Business Card Design for company

We want new business cards. We'd like something different-- yet still highly professional. Our tagline is Providing leadership, delivering success. Stock photos are ok, as long as they are relevant and look upscale.

Target Market(s)

Architecture/Business Management Consulting/Engineering Consulting

Contact Information for Business Card

dark gray background with pops of blue might be good, but you tell me. You're the designers. Rounded corners might be nice, but again, you tell me.

Font styles to use
Serif
Sans Serif

Colors
3276b5
5c5c5c
9d9d9d
fbfbfb

Requirements
Nice to have
• Something different, but still very professional.

```html
<!DOCTYPE html>
<html lang="en">
<head>
<meta charset="utf-8">
<title>Norvale Partners – Business Card</title>
<link rel="stylesheet" href="https://fonts.googleapis.com/css2?family=Poppins:wght@300;400;500;600&display=swap">
<style>
  :root {
    --brand-blue: #3276b5;
    --brand-blue-deep: #2a67a1;
    --ink-dark: #5c5c5c;
    --ink-light: #9d9d9d;
    --paper: #fbfbfb;
    --stage: #e9ecef;
  }
  * { box-sizing: border-box; margin: 0; padding: 0; }
  html, body {
    width: 1200px; height: 928px; overflow: hidden;
    background: var(--stage);
    font-family: "Poppins", sans-serif;
  }
  .stage { position: relative; width: 1200px; height: 928px; }
  .card {
    position: absolute; left: 290px; width: 620px; height: 354px;
    border-radius: 22px; overflow: hidden;
    box-shadow: 0 10px 30px rgba(0,0,0,.12);
  }
  /* Front */
  .card-front { top: 74px; background: var(--brand-blue); color: #fff; }
  .front-map {
    position: absolute; inset: 0;
    background: radial-gradient(ellipse at 55% 40%, rgba(255,255,255,.14), rgba(255,255,255,0) 65%);
  }
  .front-logo { position: absolute; left: 150px; top: 98px; font-weight: 600; line-height: 1; }
  .front-logo .name-main { display: block; font-size: 84px; letter-spacing: 2px; }
  .front-logo .name-sub { display: block; font-size: 26px; letter-spacing: 2px; margin-top: 8px; padding-left: 40px; }
  .tagline {
    position: absolute; right: 34px; bottom: 30px;
    font-size: 13px; font-weight: 400; letter-spacing: .3px;
  }
  /* Back */
  .card-back { top: 500px; background: var(--paper); color: var(--ink-dark); }
  .holder { position: absolute; left: 60px; top: 56px; }
  .holder-name { font-size: 21px; font-weight: 600; color: var(--brand-blue); letter-spacing: .5px; }
  .holder-title { font-size: 12px; font-weight: 300; color: var(--ink-dark); margin-top: 2px; }
  .back-logo {
    position: absolute; right: 44px; top: 34px; text-align: right;
    font-weight: 600; color: var(--ink-dark); line-height: 1;
  }
  .back-logo .name-main { display: block; font-size: 60px; letter-spacing: 1px; }
  .back-logo .name-sub { display: block; font-size: 19px; letter-spacing: 1.5px; margin-top: 6px; }
  .icon-tab {
    position: absolute; left: 0; top: 196px; width: 30px; height: 130px;
    background: var(--brand-blue); border-radius: 0 6px 6px 0;
    display: flex; flex-direction: column; justify-content: space-around; align-items: center;
    padding: 6px 0;
  }
  .icon-tab svg { width: 13px; height: 13px; fill: none; stroke: #fff; stroke-width: 1.6; }
  .contact-list {
    position: absolute; left: 52px; top: 200px; list-style: none;
    font-size: 14px; font-weight: 300; color: var(--ink-dark);
  }
  .contact-list li { height: 31px; line-height: 31px; }
  .contact-list .accent { color: var(--brand-blue); }
  .address {
    position: absolute; right: 44px; top: 222px; text-align: right;
    font-size: 14px; font-weight: 300; line-height: 30px;
  }
  .address .pin { display: block; margin-left: auto; margin-bottom: 2px; width: 14px; height: 18px; }
</style>
</head>
<body>
<main class="stage">

  <section class="card card-front">
    <div class="front-map" role="img" aria-label="Faint world map spread across the card"></div>
    <div class="front-logo">
      <span class="name-main">NORVALE</span>
      <span class="name-sub">PARTNERS</span>
    </div>
    <p class="tagline">Providing leadership, delivering success</p>
  </section>

  <section class="card card-back">
    <div class="holder">
      <h1 class="holder-name">DANIEL HART</h1>
      <p class="holder-title">Resident Manager</p>
    </div>

    <div class="back-logo">
      <span class="name-main">NORVALE</span>
      <span class="name-sub">PARTNERS</span>
    </div>

    <div class="icon-tab" aria-hidden="true">
      <svg viewBox="0 0 16 16"><path d="M4 2l2.5 3-1.5 1.5a8 8 0 0 0 4.5 4.5L11 9.5 14 12l-1.5 2A11 11 0 0 1 2 3.5z"/></svg>
      <svg viewBox="0 0 16 16"><rect x="4" y="2" width="8" height="4"/><rect x="2" y="6" width="12" height="6"/><rect x="4" y="10" width="8" height="4"/></svg>
      <svg viewBox="0 0 16 16"><rect x="2" y="4" width="12" height="8"/><path d="M2 4l6 5 6-5"/></svg>
      <svg viewBox="0 0 16 16"><circle cx="8" cy="8" r="6"/><path d="M2 8h12M8 2c-3 3.5-3 8.5 0 12M8 2c3 3.5 3 8.5 0 12"/></svg>
    </div>

    <ul class="contact-list">
      <li>+1 555.201.4488</li>
      <li>+1 555.461.7720</li>
      <li>info@norvalepartners.com</li>
      <li>www.<span class="accent">norvalepartners</span>.com</li>
    </ul>

    <address class="address" style="font-style:normal">
      <svg class="pin" viewBox="0 0 14 18" aria-hidden="true"><path d="M7 0a6 6 0 0 1 6 6c0 4.5-6 12-6 12S1 10.5 1 6a6 6 0 0 1 6-6z" fill="var(--brand-blue)"/><circle cx="7" cy="6" r="2.2" fill="#fff"/></svg>
      412 W 18th St. Ste 210B<br>
      Harbor City, VA 23000
    </address>
  </section>

</main>
</body>
</html>
```